A new presentation to our clients

we are a Real Estate agency, our website is www.dorelumia.com and it’s time to have a new, fashion and remarcable Business Card. we want to differentiate ourselves from other companies so we want a business card that differentiates us. we want the business card to impact our customers. in the competitive market that we have today, we have to be different and it is this difference that we seek

Target Market(s)

Real Estate Clients

Contact Information for Business Card

We search a totaly diferent card from the usual

Font styles to use
Sans Serif

Colors
e34197

Requirements
Must have
• Logo, adress, phone contact, e-mail, photo, and our website
Nice to have
• We would like to see a modern business card
Should not have
• Houses or building draws

```html
<!DOCTYPE html>
<html lang="en">
<head>
<meta charset="utf-8">
<title>Dore Lumia – Business Card</title>
<link rel="stylesheet" href="https://fonts.googleapis.com/css2?family=Lato:wght@400;700&display=swap">
<style>
  :root {
    --ink: #1e1a18;
    --paper: #fdfdff;
    --accent: #ef3a78;
    --white: #ffffff;
  }
  * { margin: 0; padding: 0; box-sizing: border-box; }
  html, body {
    width: 1200px;
    height: 720px;
    overflow: hidden;
    background: var(--paper);
  }
  .card {
    position: relative;
    width: 1200px;
    height: 720px;
    background: var(--paper);
    font-family: "Lato", sans-serif;
    overflow: hidden;
  }
  .card__shapes {
    position: absolute;
    inset: 0;
  }
  .holder {
    position: absolute;
    left: 80px;
    top: 66px;
    color: var(--white);
  }
  .holder__name {
    font-size: 55px;
    font-weight: 700;
    line-height: 1;
    letter-spacing: 0.2px;
  }
  .holder__first { color: var(--accent); }
  .holder__role {
    margin-top: 4px;
    font-size: 24px;
    font-weight: 700;
  }
  .contact {
    position: absolute;
    left: 80px;
    color: var(--white);
    font-size: 26px;
    font-weight: 700;
    letter-spacing: 0.3px;
    line-height: 1;
  }
  .contact--agency { top: 353px; }
  .contact--phone  { top: 461px; }
  .contact--web    { top: 567px; }
  .brand {
    position: absolute;
    left: 660px;
    width: 500px;
    top: 305px;
    text-align: center;
    color: var(--accent);
    font-size: 82px;
    font-weight: 700;
    line-height: 1;
    letter-spacing: 1px;
  }
</style>
</head>
<body>
<main class="card">
  <svg class="card__shapes" width="1200" height="720" viewBox="0 0 1200 720" aria-hidden="true">
    <polygon class="panel" points="0,0 480,0 663,720 0,720" fill="var(--ink)"/>

    <g class="contact-tabs" fill="var(--accent)">
      <polygon points="443,320 561,320 585,414 443,414"/>
      <polygon points="443,427 588,427 612,521 443,521"/>
      <polygon points="443,533 615,533 639,627 443,627"/>
    </g>

    <g class="divider-bars" fill="var(--white)">
      <rect x="80" y="415" width="540" height="11"/>
      <rect x="80" y="522" width="560" height="11"/>
      <rect x="80" y="628" width="590" height="11"/>
    </g>

    <g class="icon icon--pin" fill="none" stroke="var(--white)" stroke-width="2.2" stroke-linejoin="round">
      <path d="M514,402 C502,384 490,372 490,357 A24,24 0 0 1 538,357 C538,372 526,384 514,402 Z"/>
      <path d="M501,358 L514,346 L527,358"/>
      <path d="M504,356 L504,369 L524,369 L524,356"/>
      <rect x="510" y="360" width="8" height="9"/>
    </g>

    <g class="icon icon--phone" fill="none" stroke="var(--white)" stroke-width="2.5">
      <rect x="510" y="444" width="35" height="64" rx="4"/>
      <line x1="510" y1="454" x2="545" y2="454"/>
      <line x1="510" y1="498" x2="545" y2="498"/>
      <circle cx="527.5" cy="503" r="1.8" fill="var(--white)" stroke="none"/>
    </g>

    <g class="icon icon--web">
      <circle cx="541" cy="579" r="37" fill="var(--white)"/>
      <text x="541" y="585" text-anchor="middle" font-family="Lato, sans-serif" font-weight="700" font-size="19" fill="var(--accent)">www</text>
      <path d="M549,590 L559,598 L555,599 L558,605 L556,606 L553,600 L550,603 Z" fill="var(--accent)"/>
    </g>
  </svg>

  <header class="holder">
    <h1 class="holder__name"><span class="holder__first">John</span> Doe</h1>
    <p class="holder__role">President</p>
  </header>

  <p class="contact contact--agency">dorelumia agency</p>
  <p class="contact contact--phone">000 418 2690 517</p>
  <p class="contact contact--web">www.dorelumia.com</p>

  <p class="brand">Dore Lumia</p>
</main>
</body>
</html>
```